Board Game Designer needs a New Webpage

I'm a Board Game Designer and i need a simple webpage to show my products.

My games:

http://www.tablequestvault.net/boardgamedesigner/41926/marc-olivier-dravet

the actual website: http://www.tablequestvault.net/boardgamedesigner/41926/marc-olivier-dravet

I have the Theme KORIN on it. Is it possible to use it?

Industry/Entity Type

Games

Coding

Coded - Design and coding required

Font styles to use
Sans Serif

Requirements
Must have
• 1) My Logo
• 2) Clever way to show my products which are Board an Card Games.
• 3) Some Design with the Tiles - system of my Logo
• 4) Contact Form
• 5) About
• 6) Links to Social Medias
• 7) Use the colors of my Logo
Nice to have
• i would like that when i click on one button on the menu bar, there are square tiles appearing on the webpage.

```html
<!DOCTYPE html>
<html lang="en">
<head>
<meta charset="utf-8">
<title>Marc-Olivier Dravet – Board Game Designer</title>
<link rel="stylesheet" href="https://fonts.googleapis.com/css2?family=Montserrat:wght@300;400;600;700;800&family=Kaushan+Script&family=Libre+Baskerville:ital,wght@1,700&display=swap">
<style>
:root{
  --blue:#1aa3d6;
  --blue-deep:#1289c0;
  --blue-light:#3fc3ee;
  --red:#e8293b;
  --sand:#f7d88a;
  --ink:#555;
  --grey-bg:#f2f2f2;
  --footer:#222;
  --social:#3a3a3a;
  --white:#fff;
}
*{margin:0;padding:0;box-sizing:border-box}
html,body{width:1200px;height:3321px;overflow:hidden}
body{font-family:"Montserrat",sans-serif;color:var(--ink);background:var(--white);position:relative}

/* header */
.site-header{position:absolute;top:0;left:0;width:1200px;height:75px;background:var(--white);z-index:3}
.brand{position:absolute;left:88px;top:0;width:98px;height:115px;background:var(--white);border-radius:0 0 8px 8px;box-shadow:0 2px 6px rgba(0,0,0,.15);display:flex;flex-direction:column;align-items:center;justify-content:center;gap:8px}
.brand-square{width:44px;height:44px;border:3px solid var(--blue);border-radius:4px}
.brand-name{font-size:10px;font-weight:600;color:var(--blue);text-align:center;line-height:1.15}
.main-nav{position:absolute;top:22px;left:582px;display:flex;align-items:center;white-space:nowrap}
.main-nav a{font-size:12px;color:#777;text-decoration:none;text-transform:uppercase;white-space:nowrap;height:30px;line-height:26px;padding:0 14px;margin-right:22px;border:2px solid transparent;border-radius:3px}
.main-nav a:last-child{margin-right:0}
.main-nav a.is-active{border-color:var(--blue);color:var(--blue)}

/* hero */
.hero{position:absolute;top:75px;left:0;width:1200px;height:481px;background:radial-gradient(circle at 70% 40%,var(--blue-light),var(--blue) 55%,var(--blue-deep))}
.hero-text{position:absolute;left:84px;top:146px;color:var(--white)}
.hero-title{font-size:44px;font-weight:800;line-height:48px}
.hero-author{font-size:36px;font-weight:300;line-height:42px}
.hero-coauthor{font-size:36px;font-weight:800;line-height:42px}
.hero-rating{font-size:26px;font-weight:600;margin-top:6px;display:flex;align-items:center;gap:14px}
.hero-rating .stars{font-size:36px;letter-spacing:2px}
.hero-box{position:absolute;left:686px;top:25px;width:222px;height:442px;background:linear-gradient(160deg,#6a3fb0,#2b1f6b 60%,#4b2c8c);border-radius:4px;box-shadow:0 20px 40px rgba(0,0,0,.35)}

/* about */
.about{position:absolute;top:556px;left:0;width:1200px;height:447px}
.about-label{position:absolute;left:84px;top:64px;width:50px;height:320px;display:flex;align-items:center;justify-content:center}
.about-label span{transform:rotate(-90deg);white-space:nowrap;font-size:54px;font-weight:300;color:var(--blue);letter-spacing:2px}
.about-tile{position:absolute;left:200px;top:90px;width:120px;height:240px}
.about-photo{position:absolute;left:317px;top:82px;width:254px;height:283px;background:linear-gradient(160deg,#8a6a55,#c49a80 50%,#b23a3a)}
.about-body{position:absolute;left:613px;top:86px;width:494px}
.about-body h2{font-size:30px;font-weight:400;color:var(--blue);margin-bottom:12px}
.about-body p{font-size:12.5px;line-height:24px;color:#888;margin-bottom:24px}

/* games */
.games-band{position:absolute;top:1003px;left:0;width:1200px;height:115px;background:var(--red);display:flex;align-items:center;justify-content:center}
.games-band h2{font-size:44px;font-weight:300;color:var(--white)}
.game-tile{position:absolute;width:122px;height:122px;border-radius:10px;box-shadow:0 2px 5px rgba(0,0,0,.2)}
.btn-outline{position:absolute;left:549px;top:1556px;width:102px;height:40px;border:2px solid var(--blue);color:var(--blue);font-size:16px;display:flex;align-items:center;justify-content:center;border-radius:3px}

/* newsletter */
.newsletter{position:absolute;top:1647px;left:0;width:1200px;height:146px;background:var(--grey-bg)}
.newsletter h2{position:absolute;top:24px;width:100%;text-align:center;font-size:30px;font-weight:400;color:var(--blue)}
.newsletter-input{position:absolute;left:288px;top:69px;width:485px;height:44px;border:3px solid var(--blue);background:var(--white);font-size:11px;color:#333;padding-left:10px;line-height:38px}
.newsletter-btn{position:absolute;left:773px;top:69px;width:148px;height:44px;background:var(--blue);color:var(--white);font-size:18px;display:flex;align-items:center;justify-content:center}

/* news */
.news{position:absolute;top:1793px;left:0;width:1200px;height:543px;background:linear-gradient(160deg,#22aee0,var(--blue) 60%,#1494c8)}
.news h2{position:absolute;top:72px;width:100%;text-align:center;font-size:32px;font-weight:700;color:var(--white)}
.news-card{position:absolute;top:151px;width:238px;color:var(--white)}
.news-img{width:238px;height:175px;border:3px solid var(--white);border-radius:4px}
.news-card h3{font-size:19px;font-weight:700;margin-top:22px;white-space:nowrap}
.news-date{font-family:"Libre Baskerville",serif;font-style:italic;font-size:12px;margin-top:6px}
.news-card p{font-size:12px;line-height:19px;margin-top:8px;opacity:.9}
.news-more{font-size:11px;font-weight:700;margin-top:8px;display:flex;align-items:center;gap:8px}

/* contact */
.contact{position:absolute;top:2336px;left:0;width:1200px;height:498px;background:linear-gradient(180deg,var(--red) 0%,#ee5a4c 45%,var(--sand) 100%)}
.contact h2{position:absolute;top:52px;width:100%;text-align:center;font-size:32px;font-weight:700;color:var(--white)}
.field{position:absolute;left:208px;width:784px;border:2px solid rgba(255,255,255,.85)}
.field svg{position:absolute;left:12px;top:9px}
.btn-submit{position:absolute;left:538px;top:409px;width:124px;height:40px;background:var(--red);color:var(--white);font-size:19px;font-weight:700;display:flex;align-items:center;justify-content:center;border-radius:2px}

/* footer */
.site-footer{position:absolute;top:2834px;left:0;width:1200px;height:487px;background:var(--footer);color:var(--white);text-align:center}
.thanks{position:absolute;top:50px;width:100%;font-family:"Kaushan Script",cursive;font-size:64px}
.footer-email{position:absolute;left:385px;top:164px;width:430px;height:42px;background:var(--red);font-size:19px;display:flex;align-items:center;justify-content:center}
.footer-phones{position:absolute;top:230px;width:100%;font-size:15px;font-weight:600}
.footer-note{position:absolute;top:275px;left:150px;width:900px;font-size:13px;line-height:22px;color:#666}
.socials{position:absolute;top:339px;left:0;width:100%;display:flex;justify-content:center;gap:8px}
.socials a{height:33px;padding:0 8px;background:var(--social);color:var(--white);font-size:10px;font-weight:600;line-height:33px;text-decoration:none;border-radius:2px;white-space:nowrap}
.socials a.is-active{background:var(--red)}
.copyright{position:absolute;top:400px;width:100%;font-size:11px;color:#888}
.copyright em{font-style:normal;color:var(--red)}
</style>
</head>
<body>

<header class="site-header">
  <div class="brand">
    <div class="brand-square"></div>
    <div class="brand-name">MARC-OLIVIER<br>DRAVET</div>
  </div>
  <nav class="main-nav">
    <a class="is-active">Home</a><a>About me</a><a>My games</a><a>Contact me</a><a>Meet me</a>
  </nav>
</header>

<section class="hero">
  <div class="hero-text">
    <div class="hero-title">HOP TWIST: BONUS 1</div>
    <div class="hero-author">MARC-OLIVIER DRAVET</div>
    <div class="hero-coauthor">LUCIE FERMAND</div>
    <div class="hero-rating">My ratings <span class="stars">★★★★☆</span></div>
  </div>
  <div class="hero-box" role="img" aria-label="Game box of Hop Twist with colourful characters"></div>
</section>

<section class="about">
  <div class="about-label"><span>ABOUT ME</span></div>
  <svg class="about-tile" viewBox="0 0 120 240" aria-hidden="true">
    <rect x="10" y="60" width="100" height="100" fill="none" stroke="var(--blue)" stroke-width="14"/>
  </svg>
  <div class="about-photo" role="img" aria-label="Portrait photo of the designer in front of game shelves"></div>
  <div class="about-body">
    <h2>HELLO!</h2>
    <p>I design board and card games that bring friends around one table. Each project starts with a simple idea, a stack of blank tiles and many evenings of play tests.</p>
    <p>My work covers family games, quick card duels and puzzle boxes for curious players. I love clear rules, bright colours and turns that keep everyone smiling. Over the years I have teamed up with talented artists and publishers to bring these games to shelves around the world.</p>
  </div>
</section>

<section class="games-band"><h2>MY GAMES</h2></section>

<div class="game-tile" style="left:86px;top:1202px;background:linear-gradient(135deg,#5cc8e8,#f2b531)" role="img" aria-label="Game cover art"></div>
<div class="game-tile" style="left:270px;top:1202px;background:linear-gradient(135deg,#bfe3ef,#7fb0c2)" role="img" aria-label="Game cover art"></div>
<div class="game-tile" style="left:452px;top:1202px;background:linear-gradient(135deg,#d8372f,#f0a040)" role="img" aria-label="Game cover art"></div>
<div class="game-tile" style="left:633px;top:1202px;background:linear-gradient(135deg,#f2e24a,#4aa03a)" role="img" aria-label="Game cover art"></div>
<div class="game-tile" style="left:813px;top:1202px;background:linear-gradient(135deg,#e0f0f8,#e34a8a)" role="img" aria-label="Game cover art"></div>
<div class="game-tile" style="left:994px;top:1202px;background:linear-gradient(135deg,#e89a3a,#3a6a2a)" role="img" aria-label="Game cover art"></div>
<div class="game-tile" style="left:86px;top:1384px;background:linear-gradient(135deg,#2a2a6a,#c04a8a)" role="img" aria-label="Game cover art"></div>
<div class="game-tile" style="left:270px;top:1384px;background:linear-gradient(135deg,#a8d06a,#5a7a3a)" role="img" aria-label="Game cover art"></div>
<div class="game-tile" style="left:452px;top:1384px;background:linear-gradient(135deg,#f0e6d0,#2a5ab0)" role="img" aria-label="Game cover art"></div>
<div class="game-tile" style="left:633px;top:1384px;background:linear-gradient(135deg,#d8ecb8,#8ab8d8)" role="img" aria-label="Game cover art"></div>
<div class="game-tile" style="left:813px;top:1384px;background:linear-gradient(135deg,#3a9ad8,#1a3a6a)" role="img" aria-label="Game cover art"></div>
<div class="game-tile" style="left:994px;top:1384px;background:linear-gradient(135deg,#c03a6a,#2a4a8a)" role="img" aria-label="Game cover art"></div>
<div class="btn-outline">SEE ALL</div>

<section class="newsletter">
  <h2>SUBSCRIBE TO THE NEWSLETTER</h2>
  <div class="newsletter-input">Email Id :</div>
  <div class="newsletter-btn">SUBSCRIBE</div>
</section>

<section class="news">
  <h2>LATEST NEWS</h2>
  <article class="news-card" style="left:86px">
    <div class="news-img" role="img" aria-label="Photo of a board game in play" style="background:linear-gradient(135deg,#5a8a3a,#c8d07a)"></div>
    <h3>Sed ut perspiciatis</h3>
    <div class="news-date">14th January, 2016</div>
    <p>New prototype tested at the local game club</p>
    <div class="news-more">READ MORE <svg width="30" height="8" viewBox="0 0 30 8"><path d="M0 4H28M24 1l4 3-4 3" stroke="#fff" fill="none"/></svg></div>
  </article>
  <article class="news-card" style="left:350px">
    <div class="news-img" role="img" aria-label="Photo of dice and pawns" style="background:linear-gradient(135deg,#3a4a6a,#a8b0c0)"></div>
    <h3>Sed ut perspiciatis</h3>
    <div class="news-date">14th January, 2016</div>
    <p>Fresh card deck printed for the next fair</p>
    <div class="news-more">READ MORE <svg width="30" height="8" viewBox="0 0 30 8"><path d="M0 4H28M24 1l4 3-4 3" stroke="#fff" fill="none"/></svg></div>
  </article>
  <article class="news-card" style="left:613px">
    <div class="news-img" role="img" aria-label="Photo of green game pieces" style="background:linear-gradient(135deg,#e05a1a,#f0a040)"></div>
    <h3>Sed ut perspiciatis</h3>
    <div class="news-date">14th January, 2016</div>
    <p>Family game night planned for next Saturday evening</p>
    <div class="news-more">READ MORE <svg width="30" height="8" viewBox="0 0 30 8"><path d="M0 4H28M24 1l4 3-4 3" stroke="#fff" fill="none"/></svg></div>
  </article>
  <article class="news-card" style="left:877px">
    <div class="news-img" role="img" aria-label="Photo of a board with pawns" style="background:linear-gradient(135deg,#2a5a9a,#d8b080)"></div>
    <h3>Sed ut perspiciatis</h3>
    <div class="news-date">14th January, 2016</div>
    <p>Puzzle box expansion arrives in stores this spring</p>
    <div class="news-more">READ MORE <svg width="30" height="8" viewBox="0 0 30 8"><path d="M0 4H28M24 1l4 3-4 3" stroke="#fff" fill="none"/></svg></div>
  </article>
</section>

<section class="contact">
  <h2>CONTACT ME</h2>
  <div class="field" style="top:117px;height:40px"><svg width="18" height="18" viewBox="0 0 18 18"><circle cx="9" cy="5" r="4" fill="#fff"/><path d="M1 18c0-5 4-7 8-7s8 2 8 7z" fill="#fff"/></svg></div>
  <div class="field" style="top:166px;height:38px"><svg width="18" height="16" viewBox="0 0 18 16"><rect x="1" y="2" width="16" height="12" fill="#fff"/><path d="M1 2l8 7 8-7" stroke="#ee5a4c" fill="none" stroke-width="1.5"/></svg></div>
  <div class="field" style="top:213px;height:39px"><svg width="18" height="18" viewBox="0 0 18 18"><path d="M4 1l3 4-2 2c1 3 3 5 6 6l2-2 4 3-2 3C8 17 1 10 1 3z" fill="#fff"/></svg></div>
  <div class="field" style="top:261px;height:126px"><svg width="20" height="18" viewBox="0 0 20 18"><path d="M10 2c5 0 8 3 8 6s-3 6-8 6l-5 3 1-4C3 12 2 10 2 8c0-3 3-6 8-6z" fill="none" stroke="#fff" stroke-width="2"/></svg></div>
  <div class="btn-submit">SUBMIT</div>
</section>

<footer class="site-footer">
  <div class="thanks">Thank You!</div>
  <div class="footer-email">info@example.com</div>
  <div class="footer-phones">123 456 7896 &nbsp;&nbsp;|&nbsp;&nbsp; 123 456 7899</div>
  <p class="footer-note">Thanks for visiting. Write to me about new games, play tests or events and I will answer soon.</p>
  <nav class="socials" aria-label="Social media links">
    <a>Folio</a><a>Chirp</a><a class="is-active">Linkr</a><a>Tubo</a><a>Snapa</a>
  </nav>
  <div class="copyright">©<em>Marc-Olivier Dravet</em> 2016 | All Rights Reserved.</div>
</footer>

</body>
</html>
```